Tide of the Modest : Thriving amid network change by Curtis Oyelaran

Need a book cover, front, back and 3D. We would like the cover to have a digital globe that also shows blockchain/nodes. Best if it can also illustrate the idea of Tide of the modest. Please see the pictures which I have short-listed which can be potentially used for the book cover.

The book cover should look like an expert book and I have attached some graphics that we can potentially buy and use for this book cover.

The text for the back cover is attached in the docx. Some text is not finished, please leave empty spaces for this.

Target Market(s)

Those interested in technology, blockchain, business, finance and law. The more informed readers.

Industry/Entity Type

Digital

Font styles to use
Sans Serif

Colors
31a5d6
0555a3
33a6d7
3176b5
85cae6
85acd3
cee9f5
cedeed

Requirements
Must have
• We would like you to consider the images attached here for the book design. We want it to be simple, clear and like an expert book. Please refer to the docx for the back cover text. Leave some text spaces for text not yet written.
• We require, front cover, back cover and 3D. You can do the 3D after your design is selected.
Nice to have
• The cover should be classy and timeless. It should have the blockchain / nodes. Will be great if the book cover can convey the meaning of Tide of the Modest, through the text. eg. one of the images, look like a "Lanternfall" type photo, maybe the text can be somewhat Lanternfall like.
• You are welcome to suggest photos not attached here.
• Once we have identified the winner, we will proceed to purchase the photo for our use.
• Text can be Lato, but not necessary.
Should not have
• Too messy or too many ideas. Just a simple clear idea.

```html
<!DOCTYPE html>
<html lang="en">
<head>
<meta charset="utf-8">
<title>Tide of the Modest — Cover Spread</title>
<link href="https://fonts.googleapis.com/css2?family=Abril+Fatface&family=Cinzel:wght@400;600&family=Noto+Sans:wght@400&display=swap" rel="stylesheet">
<style>
  :root {
    --page-bg: #e6fbfc;
    --navy: #07152b;
    --navy-deep: #040d1c;
    --globe-core: #3176b5;
    --globe-glow: #85cae6;
    --globe-edge: #0555a3;
    --teal-frame: #1f8fae;
    --teal-deep: #13708f;
    --panel: rgba(206, 233, 245, 0.86);
    --swoosh: #85cae6;
    --accent-yellow: #f2d21b;
    --white: #ffffff;
    --ink: #1d2733;
  }
  * { box-sizing: border-box; margin: 0; padding: 0; }
  html, body { width: 1200px; height: 802px; overflow: hidden; background: var(--page-bg); }
  .spread { position: relative; width: 1200px; height: 802px; }

  /* Front cover */
  .front-cover {
    position: absolute; left: 73px; top: 30px; width: 521px; height: 740px;
    overflow: hidden;
    background: radial-gradient(ellipse at 52% 28%, #1c4f8c 0%, #0b2247 35%, var(--navy) 70%);
  }
  .front-cover .globe-art { position: absolute; inset: 0; }
  .title-block { position: absolute; left: 0; top: 56px; width: 100%; text-align: center; color: var(--white); font-family: 'Abril Fatface', serif; }
  .title-top { position: relative; font-size: 92px; line-height: 0.9; letter-spacing: -2px; }
  .title-top .title-small { position: absolute; font-size: 22px; color: var(--accent-yellow); letter-spacing: 0; bottom: 14px; margin-left: 4px; }
  .title-main { font-size: 92px; line-height: 0.85; letter-spacing: -3px; margin-top: -4px; }
  .subtitle {
    position: absolute; left: 0; width: 100%; top: 632px; text-align: center;
    font-family: 'Cinzel', serif; color: var(--white); font-size: 28px; line-height: 28px; font-weight: 400;
  }
  .byline {
    position: absolute; left: 0; width: 100%; top: 708px; text-align: center;
    font-family: 'Cinzel', serif; color: var(--white); font-size: 9px; letter-spacing: 1px;
  }

  /* Back cover */
  .back-cover {
    position: absolute; left: 604px; top: 30px; width: 521px; height: 740px; overflow: hidden;
    background:
      radial-gradient(circle at 95% 55%, rgba(49,165,214,0.55) 0%, rgba(5,85,163,0.35) 30%, transparent 60%),
      linear-gradient(180deg, var(--navy) 0%, #0a2a52 60%, var(--navy-deep) 100%);
  }
  .back-frame { position: absolute; left: 26px; top: 37px; width: 470px; height: 667px; background: var(--teal-frame); }
  .back-panel { position: absolute; left: 42px; top: 54px; width: 436px; height: 632px; background: var(--panel); }
  .portrait-slot {
    position: absolute; left: 38px; top: 46px; width: 132px; height: 132px; border-radius: 50%;
    background: var(--white); border: 6px solid var(--teal-deep); border-top-color: transparent; border-right-color: transparent;
    transform: rotate(-10deg);
  }
  .back-text {
    position: absolute; left: 58px; top: 78px; width: 406px;
    font-family: 'Noto Sans', sans-serif; font-size: 12.2px; line-height: 15.6px; color: var(--ink); text-align: justify;
  }
  .back-text .wrap-space { float: left; width: 122px; height: 140px; shape-outside: circle(50% at 40% 40%); }
  .back-text p { margin-bottom: 15.6px; }
  .corner-mark { position: absolute; left: 426px; top: 634px; width: 70px; height: 70px; background: var(--white); }
  .corner-mark::after { content: ""; position: absolute; left: 8px; top: 8px; width: 54px; height: 54px; background: var(--teal-deep); }
</style>
</head>
<body>
<main class="spread">
  <section class="front-cover">
    <svg class="globe-art" width="521" height="740" viewBox="0 0 521 740">
      <defs>
        <radialGradient id="globeFill" cx="50%" cy="35%" r="60%">
          <stop offset="0%" stop-color="#85cae6"/>
          <stop offset="35%" stop-color="#31a5d6"/>
          <stop offset="70%" stop-color="#0555a3"/>
          <stop offset="100%" stop-color="#07234a"/>
        </radialGradient>
        <radialGradient id="flare" cx="50%" cy="50%" r="50%">
          <stop offset="0%" stop-color="#ffffff" stop-opacity="0.9"/>
          <stop offset="100%" stop-color="#85cae6" stop-opacity="0"/>
        </radialGradient>
      </defs>
      <circle cx="263" cy="466" r="300" fill="url(#globeFill)" role="img" aria-label="Glowing digital globe wrapped in a network of connected nodes"/>
      <ellipse cx="268" cy="210" rx="140" ry="40" fill="url(#flare)"/>
      <path d="M0 494 C 120 590, 300 640, 521 548 L 521 740 L 0 740 Z" fill="var(--swoosh)"/>
      <path d="M0 528 C 140 620, 320 650, 521 565 L 521 740 L 0 740 Z" fill="var(--navy)"/>
    </svg>
    <div class="title-block">
      <div class="title-top">Tide<span class="title-small">of the</span></div>
      <div class="title-main">Modest</div>
    </div>
    <h2 class="subtitle">Thriving amid<br>network change</h2>
    <p class="byline">BY CURTIS OYELARAN</p>
  </section>

  <section class="back-cover">
    <div class="back-frame"></div>
    <div class="back-panel"></div>
    <div class="back-text">
      <span class="wrap-space"></span>
      <p>Most people would have heard of Corecoin and the underlying technology known as Blockchain. There have been two sides of the arguments.</p>
      <p>On the side of the bankers and the regulators, their criticism of Corecoin is that Corecoin is unregulated and not backed by any asset. On the side of the Blockchain community, the regularly heard argument is that Corecoin or CryptoAssets are limited and rare thus giving value to Corecoin or CryptoAssets.</p>
      <p>Both of these arguments are incomplete and do not explain the Blockchain evolution. The bankers and regulators are incomplete with their well intended advice because regulating an emerging historical trend caps the potential it can create in a society and that the backing of the dollar or other assets are still conditioned on various macroeconomic trend. The price of a real estate or even gold is still decided by market forces. Corecoin or cryptoassets cannot be valuable just by virtue of its limitedness - there are a lot of things that are limited that may not be valuable.</p>
      <p>Cryptoassets are valuable by virtue of how it overcomes the transactional friction that has been inherent in human history. Overcoming the transactional friction is the looking at the blockchain evolution via the eyes of an economist - that it would catalyse trading and create immense value for participating parties and create social utility for the world at large, and we are just at the beginning of the Blockchain Evolution.</p>
      <p>Cryptoassets are valuable by virtue of how it overcomes the transactional friction that has been inherent in human history. Overcoming the transactional friction is the looking at the blockchain evolution via the eyes of an economist - that it would catalyse trading and create immense value for participating parties and create social utility for the world at large, and we are just at the beginning of the Blockchain Evolution.</p>
    </div>
    <div class="portrait-slot"></div>
    <div class="corner-mark"></div>
  </section>
</main>
</body>
</html>
```